Brightfern Supports

We need an updated website that captures the comprehensive services and supports we provide to persons with developmental disabilities. We need a website design that educates families about the services we provide. We would also need a website that is user-friendly so that we could periodically update training schedules and ongoing programming.

• Thank you for submitting designs.  A few things I am hoping to see offered in the website:
• Front page highlights the services we offer (host homes, family caregiver, day program, employment program, SLS program, supported apartment program, behavior/clinical program)
• Front page also highlights any new programs we want to make prominent:  family caregiver, future restaurant employment openings, etc...
• Interactive Training Calendar
• Employee Resources page (link to carelyn, email login, etc.)
• Uniform provider application for host home providers
• Information on agency - history, goals, etc.
• Contact Information/Location

 

Fun things to include:

• Client Highlights (featuring a client story each month, etc...)
• Employee highlights (featuring a staff member...)
• link to other Brightfern business pages (Brightfern Therapy and Brightfern Restaurant)

```html
<!DOCTYPE html>
<html lang="en">
<head>
<meta charset="utf-8">
<title>Brightfern Supports</title>
<link rel="stylesheet" href="https://fonts.googleapis.com/css2?family=Oswald:wght@400;500;600&family=Open+Sans:ital,wght@0,300;0,400;0,600;0,700;1,400&display=swap">
<style>
:root{
  --red:#8c1d22;
  --red-dark:#6d1418;
  --red-soft:#a8353a;
  --ink:#3b3b3b;
  --text:#6a6a6a;
  --muted:#9a9a9a;
  --line:#e2e2e2;
  --paper:#ffffff;
  --wash:#f5f5f5;
  --slate:#3e3f41;
  --slate-dark:#2f3032;
  --blue:#4b6d90;
  --blue-dark:#3f5e7e;
  --gray-row:#8d8d8d;
  --gray-row-alt:#a5a5a5;
}
*{box-sizing:border-box;margin:0;padding:0}
html,body{width:1200px;height:3158px;overflow:hidden}
body{font-family:"Open Sans",Arial,sans-serif;color:var(--text);background:var(--paper);font-size:13px}
.wrap{width:850px;margin:0 auto;position:relative}

/* top bar */
.topbar{height:30px;background:var(--slate-dark);color:#cfcfcf;font-size:11px}
.topbar .wrap{display:flex;align-items:center;height:30px;gap:26px}
.topbar .social{display:flex;gap:8px;margin-right:auto}
.topbar .social span{width:14px;height:14px;border-radius:50%;background:#d8d8d8;display:block}
.topbar .contact{display:flex;align-items:center;gap:6px}
.topbar svg{width:12px;height:12px}

/* header */
.header{height:90px;background:var(--paper);border-bottom:1px solid var(--line)}
.header .wrap{display:flex;align-items:center;height:90px}
.brand{display:flex;align-items:center;gap:10px;margin-right:auto}
.brand-dot{width:30px;height:30px;border-radius:50%;background:var(--red)}
.brand-name{font-family:"Oswald",sans-serif;font-weight:500;font-size:19px;color:var(--red);letter-spacing:1px;line-height:1}
.nav{display:flex;gap:4px;height:90px;align-items:center}
.nav a{font-family:"Oswald",sans-serif;font-size:11px;color:var(--ink);text-decoration:none;padding:0 14px;height:90px;display:flex;align-items:center;text-transform:uppercase;letter-spacing:.6px;position:relative;text-align:center;line-height:1.3}
.nav a.active{background:var(--red);color:#fff}
.dropdown{position:absolute;top:90px;left:0;width:170px;background:var(--red);z-index:3}
.dropdown li{list-style:none;font-family:"Oswald",sans-serif;font-size:10px;color:#fff;padding:8px 12px;border-bottom:1px solid var(--red-soft);text-transform:uppercase;letter-spacing:.5px}

/* hero */
.hero{height:360px;position:relative;background:linear-gradient(100deg,#c9b8a8 0%,#e6dcd2 35%,#f1ece6 60%,#d9cfc6 100%)}
.hero-text{position:absolute;left:190px;top:112px;font-family:"Oswald",sans-serif;font-size:28px;font-weight:400;color:#fff;line-height:1.28;letter-spacing:1.5px;text-shadow:0 1px 3px rgba(0,0,0,.35)}
.hero-dots{position:absolute;left:50%;transform:translateX(-50%);bottom:28px;display:flex;gap:10px}
.hero-dots span{width:11px;height:11px;border-radius:50%;background:rgba(255,255,255,.7)}
.hero-dots span.on{background:var(--red)}

/* section title */
.section-title{font-family:"Oswald",sans-serif;font-size:30px;font-weight:600;letter-spacing:2px;color:var(--red);text-align:center;text-transform:uppercase}
.section-title::after{content:"";display:block;width:140px;height:3px;background:var(--red);margin:8px auto 0}

/* services */
.services{height:820px;background:var(--wash);padding-top:52px}
.cards{display:grid;gap:40px;margin-top:50px}
.cards.three{grid-template-columns:repeat(3,1fr)}
.cards.four{grid-template-columns:repeat(4,1fr);gap:33px;margin-top:16px}
.card{background:var(--paper);border:1px solid var(--line);box-shadow:0 1px 3px rgba(0,0,0,.08);text-align:center;padding:22px 18px 16px;height:316px;display:flex;flex-direction:column;align-items:center}
.cards.four .card{height:303px;padding:20px 14px 14px}
.card-icon{width:50px;height:50px;border-radius:50%;background:var(--red);display:flex;align-items:center;justify-content:center}
.card-icon svg{width:26px;height:26px}
.card h3{font-family:"Oswald",sans-serif;font-size:15px;font-weight:500;color:var(--red);text-transform:uppercase;letter-spacing:1px;margin:14px 0 12px;line-height:1.25;min-height:38px;display:flex;align-items:center}
.card p{font-size:11px;line-height:1.65;color:var(--text)}
.card .more{margin-top:auto;font-family:"Oswald",sans-serif;font-size:11px;color:var(--red);letter-spacing:1px;text-transform:uppercase}

/* calendar */
.schedule{height:580px;background:linear-gradient(90deg,var(--red-dark),var(--red) 50%,var(--red-dark));padding-top:40px}
.schedule .wrap{display:flex;gap:45px}
.calendar{width:540px;background:var(--paper);height:510px;overflow:hidden}
.calendar-month{font-family:"Oswald",sans-serif;font-size:42px;font-weight:600;color:var(--red);text-align:center;letter-spacing:4px;height:70px;line-height:72px}
.calendar-label{background:#c9b7b7;color:#fff;font-size:20px;font-weight:300;padding:4px 14px;height:34px}
.cal-grid{display:grid;grid-template-columns:repeat(7,1fr)}
.cal-grid .dow{background:var(--red);color:#fff;font-size:9px;font-weight:700;text-align:center;height:20px;line-height:20px;letter-spacing:.5px}
.cal-grid .day{height:77px;border-right:1px solid var(--line);border-bottom:1px solid var(--line);position:relative;padding:4px}
.cal-grid .day .num{position:absolute;top:3px;right:5px;font-size:9px;color:var(--muted)}
.cal-grid .day .event{position:absolute;left:4px;right:4px;bottom:14px;font-size:8px;line-height:1.25;color:var(--red);text-align:center}
.cal-grid .day.today{background:var(--red)}
.cal-grid .day.today .num,.cal-grid .day.today .event{color:#fff}
.programs{width:265px}
.programs h2{background:var(--paper);font-family:"Oswald",sans-serif;font-size:22px;font-weight:500;color:var(--red);letter-spacing:1.5px;text-align:center;height:70px;line-height:70px;border-bottom:3px solid var(--red)}
.programs li{list-style:none;background:var(--gray-row);color:#fff;font-size:13px;padding:8px 14px;line-height:1.3;border-bottom:1px solid rgba(255,255,255,.25)}
.programs li:nth-child(even){background:var(--gray-row-alt)}
.programs li.short{height:36px}
.programs li.long{height:58px}

/* mission */
.mission{height:150px;background:var(--blue);color:#fff;text-align:center;padding-top:22px}
.mission h2{font-family:"Oswald",sans-serif;font-size:24px;font-weight:500;letter-spacing:2px;text-transform:uppercase}
.mission h2::after{content:"";display:block;width:110px;height:2px;background:#fff;margin:6px auto 0}
.mission p{font-size:15px;font-weight:300;line-height:1.6;margin:14px auto 0;width:720px}

/* highlights */
.highlights{height:590px;background:linear-gradient(180deg,var(--slate) 0%,var(--slate-dark) 100%);padding-top:36px}
.highlights-head{display:flex;align-items:flex-end;justify-content:center;gap:120px;border-bottom:2px solid #fff;width:700px;margin:0 auto}
.highlights-head h2{font-family:"Oswald",sans-serif;font-size:26px;font-weight:500;color:#fff;letter-spacing:1.5px;padding-bottom:8px}
.month-tab{background:var(--paper);color:var(--ink);font-family:"Oswald",sans-serif;font-size:22px;font-weight:500;letter-spacing:1.5px;padding:6px 26px}
.clients{display:grid;grid-template-columns:repeat(3,1fr);gap:40px;margin-top:40px;text-align:center}
.portrait{width:140px;height:140px;border-radius:50%;border:5px solid #fff;margin:0 auto;background:radial-gradient(circle at 50% 40%,#d9b49a,#8a6a55 70%)}
.client h3{font-family:"Oswald",sans-serif;font-size:15px;font-weight:500;color:#fff;letter-spacing:.8px;margin-top:28px}
.client p{font-size:11px;line-height:1.6;color:#cfcfcf;width:220px;margin:14px auto 0;text-align:left}
.client .links{display:flex;justify-content:center;gap:10px;margin-top:18px}
.client .links span{width:18px;height:18px;border-radius:50%;background:#e6e6e6;display:block}

/* quote */
.quote{height:160px;background:var(--blue-dark);color:#fff}
.quote .wrap{display:flex;align-items:center;height:160px;gap:60px}
.quote svg{width:80px;height:64px;flex:none}
.quote blockquote{font-style:italic;font-size:16px;line-height:1.5;text-align:right;color:#e8eef4}
.quote cite{display:block;font-style:normal;font-size:11px;margin-top:8px;color:#c8d3df}

/* map */
.location{height:250px;position:relative;background:linear-gradient(135deg,#e4e6e8 0%,#d4d8dc 50%,#e9ebec 100%)}
.map-card{position:absolute;left:0;top:0;width:150px;height:90px;background:var(--paper);padding:10px 12px;font-size:10px;line-height:1.5;color:var(--ink);box-shadow:0 1px 4px rgba(0,0,0,.15)}
.map-card strong{display:block;font-size:11px}
.location-btn{position:absolute;left:50%;top:52px;transform:translateX(-50%);background:var(--red);color:#fff;font-family:"Oswald",sans-serif;font-size:14px;letter-spacing:1.5px;padding:10px 30px}
.pin{position:absolute;left:50%;top:110px;transform:translateX(-50%);width:42px;height:58px}

/* footer */
.footer{height:98px;background:var(--slate);color:#bdbdbd;font-size:9px;padding-top:14px}
.footer .wrap{display:grid;grid-template-columns:1.1fr .9fr 1.5fr .8fr;gap:30px}
.footer h4{font-family:"Oswald",sans-serif;font-size:10px;font-weight:500;color:#fff;letter-spacing:1px;margin-bottom:6px;text-transform:uppercase}
.footer p,.footer li{line-height:1.5;list-style:none}
.newsletter{display:flex;margin-top:6px}
.newsletter span{flex:1;height:18px;background:#fff}
.newsletter b{width:60px;height:18px;background:var(--red);color:#fff;font-size:9px;text-align:center;line-height:18px;font-weight:600}
.legal{height:30px;background:var(--slate-dark);color:#9b9b9b;font-size:9px;text-align:center;line-height:30px;letter-spacing:.5px}
</style>
</head>
<body>

<div class="topbar">
  <div class="wrap">
    <div class="social"><span></span><span></span><span></span><span></span></div>
    <div class="contact">
      <svg viewBox="0 0 24 24" fill="#cfcfcf"><path d="M6.6 10.8a15 15 0 0 0 6.6 6.6l2.2-2.2c.3-.3.7-.4 1-.2 1.1.4 2.3.6 3.6.6.6 0 1 .4 1 1V20c0 .6-.4 1-1 1A17 17 0 0 1 3 4c0-.6.4-1 1-1h3.5c.6 0 1 .4 1 1 0 1.3.2 2.5.6 3.6.1.3 0 .7-.2 1z"/></svg>
      <span>Call us: (555) 014-2200</span>
    </div>
    <div class="contact">
      <svg viewBox="0 0 24 24" fill="none" stroke="#cfcfcf" stroke-width="2"><rect x="3" y="5" width="18" height="14"/><path d="M3 6l9 7 9-7"/></svg>
      <span>info@brightfern.org</span>
    </div>
    <div class="contact">
      <svg viewBox="0 0 24 24" fill="none" stroke="#cfcfcf" stroke-width="2.5"><circle cx="10" cy="10" r="6"/><path d="M15 15l6 6"/></svg>
      <span>SEARCH</span>
    </div>
  </div>
</div>

<header class="header">
  <div class="wrap">
    <div class="brand">
      <span class="brand-dot"></span>
      <span class="brand-name">BRIGHTFERN SUPPORTS</span>
    </div>
    <nav class="nav">
      <a>Host Homes</a>
      <a>Services &amp;<br>Supports</a>
      <a class="active">Programs
        <ul class="dropdown">
          <li>Employment Program</li>
          <li>Supported Apartment Program</li>
          <li>SLS Program</li>
          <li>Behavior Program</li>
        </ul>
      </a>
      <a>About Us</a>
      <a>Resources</a>
      <a>Contact Us</a>
    </nav>
  </div>
</header>

<section class="hero" role="img" aria-label="Photo of a caregiver smiling with an elderly woman">
  <div class="hero-text">BUILDING ABILITIES<br>CREATING OPPORTUNITIES<br>DEVELOPING RELATIONSHIPS</div>
  <div class="hero-dots"><span class="on"></span><span></span><span></span><span></span></div>
</section>

<section class="services">
  <h2 class="section-title">Services</h2>
  <div class="wrap">
    <div class="cards three">
      <article class="card">
        <div class="card-icon"><svg viewBox="0 0 24 24" fill="#fff"><path d="M12 3l9 8h-3v9h-4v-6h-4v6H6v-9H3z"/></svg></div>
        <h3>Host Home Services</h3>
        <p>We place people with caring host families in their own community, offering a safe, stable home and daily support that helps each person grow with confidence.</p>
        <span class="more">Read More</span>
      </article>
      <article class="card">
        <div class="card-icon"><svg viewBox="0 0 24 24" fill="#fff"><circle cx="12" cy="7" r="4"/><path d="M4 21c0-4.4 3.6-8 8-8s8 3.6 8 8z"/></svg></div>
        <h3>Family Caregiver</h3>
        <p>Families who care for a loved one at home receive training, guidance and steady support from our team, so that care stays personal and lasting.</p>
        <span class="more">Read More</span>
      </article>
      <article class="card">
        <div class="card-icon"><svg viewBox="0 0 24 24" fill="#fff"><circle cx="8" cy="8" r="3"/><circle cx="16" cy="8" r="3"/><path d="M2 20c0-3.3 2.7-6 6-6s6 2.7 6 6zM12 20c0-3.3 1.8-6 4-6 3.3 0 6 2.7 6 6z"/></svg></div>
        <h3>Supported Apartment Program</h3>
        <p>Residents live in their own apartment with staff close by, building skills for cooking, budgeting and daily routines while keeping their independence.</p>
        <span class="more">Read More</span>
      </article>
    </div>
    <div class="cards four">
      <article class="card">
        <div class="card-icon"><svg viewBox="0 0 24 24" fill="#fff"><path d="M9 4h6v3h5v12H4V7h5zm2 0v3h2V4z"/></svg></div>
        <h3>Employment Program</h3>
        <p>We help people find and keep jobs that fit their goals, with coaching on the job and close ties to local employers.</p>
        <span class="more">Read More</span>
      </article>
      <article class="card">
        <div class="card-icon"><svg viewBox="0 0 24 24" fill="#fff"><path d="M12 2l3 7h7l-5.6 4.3L18.5 21 12 16.6 5.5 21l2.1-7.7L2 9h7z"/></svg></div>
        <h3>SLS Program</h3>
        <p>Supported living services give people the help they need at home and in town, shaped around their own plans.</p>
        <span class="more">Read More</span>
      </article>
      <article class="card">
        <div class="card-icon"><svg viewBox="0 0 24 24" fill="#fff"><path d="M4 6h16v14H4zM7 3v4M17 3v4" stroke="#fff" stroke-width="2"/><rect x="6" y="10" width="12" height="8" fill="#8c1d22"/></svg></div>
        <h3>Day Program</h3>
        <p>Daytime activities, outings and classes build friendships and new skills in a welcoming, structured setting.</p>
        <span class="more">Read More</span>
      </article>
      <article class="card">
        <div class="card-icon"><svg viewBox="0 0 24 24" fill="#fff"><circle cx="12" cy="7" r="4"/><path d="M4 21c0-4.4 3.6-8 8-8s8 3.6 8 8z"/></svg></div>
        <h3>Behavior Program</h3>
        <p>Our clinical team offers behavior support plans and counseling that promote positive, lasting change.</p>
        <span class="more">Read More</span>
      </article>
    </div>
  </div>
</section>

<section class="schedule">
  <div class="wrap">
    <div class="calendar">
      <div class="calendar-month">APRIL</div>
      <div class="calendar-label">Training Calendar</div>
      <div class="cal-grid">
        <div class="dow">SUN</div><div class="dow">MON</div><div class="dow">TUE</div><div class="dow">WED</div><div class="dow">THU</div><div class="dow">FRI</div><div class="dow">SAT</div>
        <div class="day"><span class="num">29</span></div>
        <div class="day"><span class="num">30</span></div>
        <div class="day"><span class="num">31</span></div>
        <div class="day"><span class="num">1</span></div>
        <div class="day"><span class="num">2</span></div>
        <div class="day"><span class="num">3</span></div>
        <div class="day"><span class="num">4</span></div>
        <div class="day"><span class="num">5</span></div>
        <div class="day"><span class="num">6</span><span class="event">Training Update<br>9:00 am</span></div>
        <div class="day"><span class="num">7</span></div>
        <div class="day"><span class="num">8</span><span class="event">Training Update<br>1:00 pm</span></div>
        <div class="day"><span class="num">9</span></div>
        <div class="day"><span class="num">10</span><span class="event">Training Update<br>10:00 am</span></div>
        <div class="day"><span class="num">11</span></div>
        <div class="day"><span class="num">12</span><span class="event">Training Update<br>9:00 am</span></div>
        <div class="day"><span class="num">13</span></div>
        <div class="day"><span class="num">14</span><span class="event">Training Update<br>2:00 pm</span></div>
        <div class="day today"><span class="num">15</span></div>
        <div class="day"><span class="num">16</span><span class="event">Training Update<br>9:00 am</span></div>
        <div class="day"><span class="num">17</span></div>
        <div class="day"><span class="num">18</span></div>
        <div class="day"><span class="num">19</span></div>
        <div class="day"><span class="num">20</span><span class="event">Training Update<br>11:00 am</span></div>
        <div class="day"><span class="num">21</span></div>
        <div class="day"><span class="num">22</span><span class="event">Training Update<br>9:00 am</span></div>
        <div class="day"><span class="num">23</span></div>
        <div class="day"><span class="num">24</span></div>
        <div class="day"><span class="num">25</span></div>
        <div class="day"><span class="num">26</span></div>
        <div class="day"><span class="num">27</span><span class="event">Training Update<br>9:00 am</span></div>
        <div class="day"><span class="num">28</span></div>
        <div class="day"><span class="num">29</span><span class="event">Training Update<br>3:00 pm</span></div>
        <div class="day"><span class="num">30</span></div>
        <div class="day"><span class="num">1</span></div>
        <div class="day"><span class="num">2</span></div>
      </div>
    </div>
    <aside class="programs">
      <h2>PROGRAMS</h2>
      <ul>
        <li class="short">Family Caregiver</li>
        <li class="long">Future Restaurant Employment openings</li>
        <li class="short">Future Restaurant</li>
        <li class="long">Future Restaurant Employment openings</li>
        <li class="short">Future Restaurant</li>
        <li class="long">Future Restaurant Employment openings</li>
        <li class="short">Future Restaurant</li>
        <li class="long">Future Restaurant Employment openings</li>
      </ul>
    </aside>
  </div>
</section>

<section class="mission">
  <h2>Mission Statement</h2>
  <p>To promote relationships, attachment, positive behaviors, and resource development to create opportunities and improve the lives of people living with disabilities.</p>
</section>

<section class="highlights">
  <div class="highlights-head">
    <h2>CLIENT HIGHLIGHTS</h2>
    <div class="month-tab">APRIL</div>
  </div>
  <div class="wrap">
    <div class="clients">
      <div class="client">
        <div class="portrait" role="img" aria-label="Portrait photo of a smiling man"></div>
        <h3>LENA MARWOOD, MA, LPC</h3>
        <p>Lena has spent over ten years working with people with disabilities and their families. She is a licensed professional counselor who leads our clinical team with care.</p>
        <div class="links"><span></span><span></span><span></span></div>
      </div>
      <div class="client">
        <div class="portrait" role="img" aria-label="Portrait photo of a smiling woman"></div>
        <h3>LENA MARWOOD, MA, LPC</h3>
        <p>Lena has spent over ten years working with people with disabilities and their families. She is a licensed professional counselor who leads our clinical team with care.</p>
        <div class="links"><span></span><span></span><span></span></div>
      </div>
      <div class="client">
        <div class="portrait" role="img" aria-label="Portrait photo of a smiling woman"></div>
        <h3>LENA MARWOOD, MA, LPC</h3>
        <p>Lena has spent over ten years working with people with disabilities and their families. She is a licensed professional counselor who leads our clinical team with care.</p>
        <div class="links"><span></span><span></span><span></span></div>
      </div>
    </div>
  </div>
</section>

<section class="quote">
  <div class="wrap">
    <svg viewBox="0 0 80 64" aria-hidden="true"><path d="M4 4h72v42H30L14 60V46H4z" fill="#7e95ad"/><path d="M16 18h48M16 28h36" stroke="#4b6d90" stroke-width="4"/></svg>
    <blockquote>"Praesent vestibulum aenean nonummy hendrerit mauris. Whether you need a motor for a precise medical application."
      <cite>Dale Orwin, Northgate Motion Works</cite>
    </blockquote>
  </div>
</section>

<section class="location" role="img" aria-label="Street map showing the agency office location">
  <div class="map-card"><strong>Brightfern Supports</strong>1420 Fernway Drive<br>Hollis Springs, CO 80000<br>(555) 014-2200</div>
  <div class="location-btn">OUR LOCATION</div>
  <svg class="pin" viewBox="0 0 42 58"><path d="M21 2C10.5 2 3 10 3 20c0 13 18 36 18 36s18-23 18-36C39 10 31.5 2 21 2z" fill="#8c1d22"/><circle cx="21" cy="20" r="7" fill="#fff"/></svg>
</section>

<footer class="footer">
  <div class="wrap">
    <div>
      <h4>About Us</h4>
      <p>1420 Fernway Drive<br>Hollis Springs, CO 80000<br>Phone: (555) 014-2200<br>Fax: (555) 014-2201</p>
    </div>
    <div>
      <h4>Company</h4>
      <ul><li>About</li><li>Careers</li><li>Programs</li><li>Contact</li></ul>
    </div>
    <div>
      <h4>Subscribe to our newsletter</h4>
      <p>Get program news and training updates by email.</p>
      <div class="newsletter"><span></span><b>SUBMIT</b></div>
    </div>
    <div>
      <h4>Quick Support</h4>
      <ul><li>Forms</li><li>Staff Login</li><li>Carelyn</li><li>Help</li></ul>
    </div>
  </div>
</footer>
<div class="legal">© 2024 BRIGHTFERN SUPPORTS · ALL RIGHTS RESERVED · PRIVACY POLICY</div>

</body>
</html>
```